Plakat-Design Workshop gegen Prüfungsangst
Zielgruppe
Prüfungsangst überwinden mittels Workshops: 'Selbsthypnose erlernen'
Zielgruppe Studenten
Schweißausbrüche, Blackout, und Resignation.
Viele kennen diese unangenehmen Momente, wenn eine Prüfung begonnen hat und die Aufgabenstellungen scheinbar unlösbar sind.
Dann ist Entspannung nahezu unmöglich. Das Stresshormon Cortisol wurde bereits ausgeschüttet. Es beeinträchtigt die Erinnerung an das Gelernte.
Die mentale Vorbereitung sollte schon viel eher ansetzen, wenn es noch nicht zu spät ist. Wenn der Körper noch nicht verkrampft ist.
Selbsthypnose vor Prüfungen ist hier eine tolle Möglichkeit.
Mit Hilfe einer geführten Selbsthypnoseanleitung ist es Dir möglich Dein Unterbewusstsein so zu programmieren, dass diese Übererregungszustände vor Prüfungssituationen deutlich reduziert werden.
Aufgabenstellung
DINA 4 Plakat, 'Prüfungsangst?' mit einem Freifeld, wo man Ort, Datum und Zeit der Veranstaltung 'Selbsthypnose erlernen'
(Selbstsicher in die Prüfung) eindrucken kann.
darunter:
Anmeldung: Tel: 01563 8274015
Dipl. Sportl. Henrik Malow Mentaltraining
weitere Infos auch über Einzelsitzungen: www.malow-trance.de

```html
<!DOCTYPE html>
<html lang="de">
<head>
<meta charset="utf-8">
<title>Prüfungsangst? – Workshop Selbsthypnose</title>
<link rel="stylesheet" href="https://fonts.googleapis.com/css2?family=Hind:wght@400;500;600;700&display=swap">
<style>
  :root {
    --red: #e1302a;
    --ink: #111111;
    --paper: #ffffff;
    --rule: #b5b5b5;
    --photo-warm-a: #b8733a;
    --photo-warm-b: #d89a5c;
    --photo-cool: #8fa3bd;
    --portrait-a: #c9c9c7;
    --portrait-b: #6f747c;
    --badge-teal: #147f8c;
    --badge-ring: #d6e3e8;
  }
  * { margin: 0; padding: 0; box-sizing: border-box; }
  html, body { width: 881px; height: 1200px; overflow: hidden; background: var(--paper); }
  .poster {
    position: relative;
    width: 881px; height: 1200px;
    background: var(--paper);
    font-family: "Hind", sans-serif;
    color: var(--ink);
  }
  .hero-photo {
    position: absolute; left: 0; top: 0; width: 881px; height: 381px;
    background: linear-gradient(100deg, var(--photo-cool) 0%, #c9b7a6 28%, var(--photo-warm-a) 55%, var(--photo-warm-b) 80%, #a9652e 100%);
  }
  .hero-rule {
    position: absolute; left: 0; top: 389px; width: 881px; height: 6px; background: var(--red);
  }
  .headline {
    position: absolute; left: 28px; top: 400px;
    font-size: 122px; font-weight: 500; color: var(--red);
    letter-spacing: -1px; line-height: 1;
  }
  .subhead {
    position: absolute; left: 31px; top: 560px;
    font-size: 37px; font-weight: 600; line-height: 1; letter-spacing: -0.2px;
  }
  .intro {
    position: absolute; left: 31px; top: 605px; width: 840px;
    font-size: 27.5px; font-weight: 400; line-height: 36px;
  }
  .claim {
    position: absolute; left: 31px; top: 712px;
    font-size: 63px; font-weight: 600; color: var(--red); line-height: 1; letter-spacing: -0.5px;
  }
  .portrait {
    position: absolute; left: 33px; top: 810px; width: 247px; height: 340px;
    background: linear-gradient(180deg, var(--portrait-a) 0%, #a7a9ab 45%, var(--portrait-b) 100%);
  }
  .seal { position: absolute; left: 226px; top: 1032px; width: 158px; height: 158px; }
  .fill-fields { position: absolute; left: 407px; top: 800px; width: 442px; }
  .field {
    display: flex; align-items: flex-end; height: 56px; margin-bottom: 7px;
    font-size: 44px; line-height: 1;
  }
  .field .line { flex: 1; height: 3px; background: var(--rule); margin-left: 4px; margin-bottom: 6px; }
  .registration {
    position: absolute; left: 407px; top: 1010px;
    font-size: 23.5px; line-height: 28.5px;
  }
  .registration strong { font-weight: 600; }
  .footer-band {
    position: absolute; left: 0; top: 1159px; width: 881px; height: 41px; background: var(--red);
  }
</style>
</head>
<body>
<div class="poster">
  <div class="hero-photo" role="img" aria-label="Foto: gestresste Studentin hält sich den Kopf in einer Prüfungshalle, dahinter weitere schreibende Studierende"></div>
  <div class="hero-rule"></div>

  <h1 class="headline">Prüfungsangst?</h1>
  <p class="subhead">Schweißausbrüche, Blackout &amp; Resignation?</p>
  <p class="intro">Im Workshop "Selbsthypnose" lernst Du Strategien, solche Übererregungszustände vor Prüfungen deutlich zu reduzieren.</p>
  <p class="claim">Selbstsicher in die Prüfung!</p>

  <div class="portrait" role="img" aria-label="Porträtfoto des Mentaltrainers vor einer Betonwand"></div>

  <svg class="seal" viewBox="0 0 158 158" aria-hidden="true">
    <circle cx="79" cy="79" r="79" fill="#ffffff"/>
    <circle cx="79" cy="79" r="70" fill="var(--badge-ring)" stroke="var(--badge-teal)" stroke-width="2"/>
    <circle cx="79" cy="79" r="40" fill="var(--badge-teal)"/>
  </svg>

  <div class="fill-fields">
    <div class="field">Ort:<span class="line"></span></div>
    <div class="field">Datum:<span class="line"></span></div>
    <div class="field">Zeit:<span class="line"></span></div>
  </div>

  <div class="registration">
    <strong>Anmeldung:</strong><br>
    Tel: 01563 8274015<br>
    Dipl. Sportl. Henrik Malow Mentaltraining<br>
    weitere Infos auch über Einzelsitzungen:<br>
    <strong>www.malow-trance.de</strong>
  </div>

  <div class="footer-band"></div>
</div>
</body>
</html>
```